New Corporate Business Card - Velmorabelle

What we need:
We need a new corporate business card.
We want a new template that we can change by ourself.
We want business card modern and minimalist but that looks professional.
We will print it in 300 gr soft-touch.
Why not a white side with the logo and a red/grey side with the content?
Why not a grey side and a red side like our logo?
I am sure that you have better idea than ours that's the reason we come here.

Who we are:
We are a private label company in cosmetics based in Switzerland. We work in BtoB. We make skin care products for other brands.

Target Market(s)

B to B - Worldwide - any gender

Industry/Entity Type

Cosmetics

Contact Information for Business Card

Side 1:
Logo
Your Swiss Private Label Manufacturer or www.velmorabelle.ch

Side 2:
Name and surname (Example: Lucien Marchetaz)
Job Description (General Manager)
Telephone (+41 32 918 64 00)
Direct (+41 32 918 64 64)
Email (lucien.marchetaz@velmorabelle.ch)
Chemin des Prés-Fleuris 14, 2000 Neuchâtel, Switzerland
www.velmorabelle.ch

Font styles to use
Serif
Sans Serif

Requirements
Must have
• You can use 4 colors: white, red, grey and/or black .
Should not have
• Too much colors, too much things. We want it simple!

```html
<!DOCTYPE html>
<html lang="en">
<head>
<meta charset="utf-8">
<title>Velmorabelle – Business Card</title>
<link rel="stylesheet" href="https://fonts.googleapis.com/css2?family=Open+Sans:wght@300;400;600;700&display=swap">
<style>
  :root {
    --backdrop: #e4e4e4;
    --card: #ffffff;
    --red: #e32636;
    --grey: #b3b3b3;
    --grey-text: #a6a6a6;
    --ink: #2b2b2b;
    --dark: #333333;
    --divider: #c8c8c8;
  }
  * { box-sizing: border-box; margin: 0; padding: 0; }
  html, body { width: 1200px; height: 856px; overflow: hidden; }
  body {
    background: var(--backdrop);
    font-family: "Open Sans", Arial, sans-serif;
    position: relative;
  }
  .card {
    position: absolute;
    left: 285px;
    width: 630px;
    height: 360px;
    background: var(--card);
    border-radius: 28px;
    overflow: hidden;
    box-shadow: 0 6px 18px rgba(0,0,0,0.12);
  }
  .card--front { top: 40px; }
  .card--back { top: 456px; }
  .card__edge { position: absolute; left: 0; bottom: 0; width: 100%; height: 70px; }

  /* Front side */
  .brand {
    position: absolute;
    display: flex;
    align-items: center;
    gap: 18px;
  }
  .brand__mark { background: var(--red); flex: none; }
  .brand__name { color: var(--ink); font-weight: 300; letter-spacing: 0.06em; }
  .card--front .brand { left: 0; right: 0; top: 120px; justify-content: center; }
  .card--front .brand__mark { width: 46px; height: 46px; }
  .card--front .brand__name { font-size: 52px; }
  .front__url {
    position: absolute;
    right: 44px;
    bottom: 10px;
    color: #fff;
    font-weight: 700;
    font-size: 17px;
    letter-spacing: 0.01em;
  }

  /* Back side */
  .identity { position: absolute; left: 40px; top: 104px; width: 290px; }
  .card--back .brand { position: static; gap: 12px; }
  .card--back .brand__mark { width: 26px; height: 26px; }
  .card--back .brand__name { font-size: 30px; }
  .person { margin-top: 22px; }
  .person__name { color: var(--red); font-weight: 700; font-size: 19px; display: block; }
  .person__role { color: var(--grey-text); font-size: 15px; font-weight: 400; }
  .divider {
    position: absolute; left: 342px; top: 70px; width: 1px; height: 150px;
    background: var(--divider);
  }
  .contacts { position: absolute; left: 366px; top: 80px; list-style: none; }
  .contacts li {
    display: flex; align-items: flex-start; gap: 12px;
    color: var(--ink); font-size: 13.5px; line-height: 1.5; margin-bottom: 8px;
  }
  .contacts svg { flex: none; width: 16px; height: 16px; margin-top: 2px; }
</style>
</head>
<body>

<section class="card card--front" aria-label="Business card, logo side">
  <div class="brand">
    <span class="brand__mark"></span>
    <span class="brand__name">Velmorabelle</span>
  </div>
  <svg class="card__edge" viewBox="0 0 630 70" preserveAspectRatio="none" aria-hidden="true">
    <rect x="0" y="62" width="630" height="8" fill="var(--dark)"/>
    <path d="M300 70 L300 50 Q300 38 312 38 L620 38 Q630 38 630 48 L630 70 Z" fill="var(--dark)"/>
  </svg>
  <span class="front__url">www.velmorabelle.ch</span>
</section>

<section class="card card--back" aria-label="Business card, contact side">
  <div class="identity">
    <div class="brand">
      <span class="brand__mark"></span>
      <span class="brand__name">Velmorabelle</span>
    </div>
    <p class="person">
      <span class="person__name">Lucien Marchetaz</span>
      <span class="person__role">General Manager</span>
    </p>
  </div>

  <span class="divider"></span>

  <ul class="contacts">
    <li>
      <svg viewBox="0 0 16 16" aria-hidden="true"><path d="M8 1a5 5 0 0 0-5 5c0 3.6 5 9 5 9s5-5.4 5-9a5 5 0 0 0-5-5z" fill="var(--red)"/><circle cx="8" cy="6" r="1.8" fill="#fff"/></svg>
      <span>Chemin des Prés-Fleuris 14,<br>2000 Neuchâtel, Switzerland</span>
    </li>
    <li>
      <svg viewBox="0 0 16 16" aria-hidden="true"><rect x="2" y="6" width="12" height="8" rx="2" fill="var(--red)"/><path d="M1 6 Q8 0 15 6" stroke="var(--red)" stroke-width="2" fill="none"/><circle cx="8" cy="10" r="2" fill="#fff"/></svg>
      <span>+41 32 918 64 00</span>
    </li>
    <li>
      <svg viewBox="0 0 16 16" aria-hidden="true"><rect x="2" y="6" width="12" height="8" rx="2" fill="var(--red)"/><path d="M1 6 Q8 0 15 6" stroke="var(--red)" stroke-width="2" fill="none"/><circle cx="8" cy="10" r="2" fill="#fff"/></svg>
      <span>+41 32 918 64 64</span>
    </li>
    <li>
      <svg viewBox="0 0 16 16" aria-hidden="true"><rect x="1" y="3" width="14" height="10" rx="2" fill="var(--red)"/><path d="M2 4.5 L8 9 L14 4.5" stroke="#fff" stroke-width="1.4" fill="none"/></svg>
      <span>lucien.marchetaz@velmorabelle.ch</span>
    </li>
  </ul>

  <svg class="card__edge" viewBox="0 0 630 70" preserveAspectRatio="none" aria-hidden="true">
    <rect x="0" y="60" width="470" height="10" fill="var(--red)"/>
    <rect x="470" y="60" width="160" height="10" fill="var(--dark)"/>
  </svg>
</section>

</body>
</html>
```